Korvel Banner Design

We need banners for new company Korvel Holdings Limited located in Hong Kong. Korvel is an global online business platform, needs clean white, blue and red color mix banners.
Updates

Reason: I am extending for final design

Target Market(s)

Korvel an online Business Company have a target home based business owners and DIY website seekers.

Industry/Entity Type

Business

Colors
0355a3
ec2027
ffffff

Requirements
Must have
• Free Sign Up Button and Korvel Logo

```html
<!DOCTYPE html>
<html lang="en">
<head>
<meta charset="utf-8">
<title>Korvel Banner Set</title>
<link rel="stylesheet" href="https://fonts.googleapis.com/css2?family=Roboto+Condensed:wght@400;500&display=swap">
<style>
  :root {
    --brand-blue: #0355a3;
    --brand-red: #ec2027;
    --white: #ffffff;
    --frame: #1d1d1d;
    --logo-grey: #8c9299;
    --logo-light: #c9ced4;
    --wave: #bcd9f2;
  }
  * { box-sizing: border-box; margin: 0; padding: 0; }
  html, body { width: 1200px; height: 1200px; overflow: hidden; background: var(--white); }
  body { position: relative; font-family: "Roboto Condensed", "Arial Narrow", sans-serif; color: var(--white); }

  .banner { position: absolute; border: 1px solid var(--frame); background: var(--white); overflow: hidden; }
  .banner .bands { position: absolute; inset: 0; width: 100%; height: 100%; }
  .banner .band-blue { fill: var(--brand-blue); }
  .banner .band-red { fill: var(--brand-red); }
  .banner > *:not(.bands) { position: absolute; }

  .wave-area {
    background: radial-gradient(ellipse at 80% 50%, rgba(188,217,242,0.75), rgba(188,217,242,0.15) 60%, rgba(255,255,255,0) 80%);
  }
  .line-area {
    background: linear-gradient(135deg, rgba(255,255,255,0.08), rgba(255,255,255,0.28) 50%, rgba(255,255,255,0.06));
  }

  .headline { text-transform: uppercase; font-weight: 400; color: var(--white); white-space: nowrap; }
  .subline { text-transform: uppercase; color: var(--white); white-space: nowrap; }
  .tagline { text-transform: uppercase; color: var(--brand-blue); white-space: nowrap; }
  .brand { font-weight: 500; letter-spacing: 0.04em; color: var(--logo-grey); white-space: nowrap; }
  .brand.on-blue { color: var(--logo-light); }
  .signup {
    background: var(--brand-red); color: var(--white); text-transform: uppercase;
    display: flex; align-items: center; justify-content: center; gap: 0.35em; white-space: nowrap;
  }
  .signup svg { fill: var(--white); }

  /* Skyscraper 160x600 */
  .sky { left: 935px; top: 63px; width: 239px; height: 899px; }
  .sky .brand { left: 0; width: 100%; text-align: center; top: 24px; font-size: 25px; }
  .sky .headline { left: 19px; top: 40px; font-size: 24px; line-height: 33px; }
  .sky .subline { left: 19px; top: 252px; font-size: 16.5px; line-height: 24px; }
  .sky .wave-area { right: 0; top: 400px; width: 150px; height: 499px; }
  .sky .tagline { left: 19px; top: 564px; font-size: 27px; line-height: 36px; }
  .sky .signup { left: 19px; top: 756px; width: 147px; height: 36px; font-size: 16.5px; }

  /* Medium rectangle 300x250 */
  .rect { left: 57px; top: 721px; width: 375px; height: 375px; }
  .rect .headline { left: 25px; top: 12px; font-size: 30px; line-height: 36px; }
  .rect .subline { left: 25px; top: 140px; font-size: 16.5px; }
  .rect .wave-area { right: 0; top: 190px; width: 170px; height: 185px; }
  .rect .tagline { left: 25px; top: 225px; font-size: 27px; line-height: 36px; }
  .rect .brand { left: 25px; top: 311px; font-size: 22px; }
  .rect .signup { left: 228px; top: 311px; width: 146px; height: 35px; font-size: 16.5px; }

  /* Square 250x250 */
  .square { left: 472px; top: 774px; width: 188px; height: 186px; }
  .square .headline { left: 9px; top: 10px; font-size: 21px; line-height: 22.5px; }
  .square .tagline { left: 9px; top: 111px; font-size: 15px; line-height: 21px; }
  .square .brand { left: 7px; top: 162px; font-size: 13.5px; }
  .square .signup { left: 97px; top: 160px; width: 90px; height: 20px; font-size: 11px; }

  /* Vertical rectangle */
  .vertical { left: 708px; top: 721px; width: 179px; height: 239px; }
  .vertical .headline { left: 10px; top: 9px; font-size: 16.5px; line-height: 24px; }
  .vertical .wave-area { right: 0; top: 100px; width: 70px; height: 139px; }
  .vertical .tagline { left: 10px; top: 115px; font-size: 16.5px; line-height: 24px; }
  .vertical .brand { left: 5px; top: 205px; font-size: 13.5px; }
  .vertical .signup { left: 88px; top: 203px; width: 90px; height: 22px; font-size: 11px; }

  /* Small rectangle */
  .small { left: 708px; top: 531px; width: 179px; height: 135px; }
  .small .headline { left: 9px; top: 6px; font-size: 15px; line-height: 21px; }
  .small .tagline { left: 11px; top: 70px; font-size: 13.5px; line-height: 18px; }
  .small .brand { left: 7px; top: 110px; font-size: 13px; }
  .small .signup { left: 96px; top: 109px; width: 82px; height: 19px; font-size: 10.5px; }

  /* Leaderboard */
  .leader { left: 472px; top: 1002px; width: 701px; height: 89px; }
  .leader .line-area { left: 0; top: 0; width: 68px; height: 89px; }
  .leader .headline { left: 81px; top: 12px; font-size: 21px; line-height: 26px; }
  .leader .subline { left: 81px; top: 44px; font-size: 15px; }
  .leader .brand { left: 556px; top: 7px; font-size: 25px; }
  .leader .signup { left: 553px; top: 48px; width: 147px; height: 34px; font-size: 17px; }
</style>
</head>
<body>

<section class="banner sky" aria-label="Korvel skyscraper banner">
  <svg class="bands" viewBox="0 0 239 899" preserveAspectRatio="none" aria-hidden="true">
    <polygon class="band-blue" points="0,0 239,0 239,366 0,394"/>
    <polygon class="band-red" points="0,394 239,366 239,399 0,429"/>
  </svg>
  <div class="wave-area" role="img" aria-label="Soft light blue flowing line decoration"></div>
  <div class="brand on-blue">KORVEL</div>
  <h2 class="headline" style="top:90px">Create your own<br>ecommerce<br>website<br>@minimum<br>$10/month</h2>
  <p class="subline">&amp; Start earning at<br>the same time.</p>
  <p class="tagline">Revolutionary<br>single line<br>affiliate<br>program</p>
  <div class="signup">Free sign up <svg width="6" height="8" viewBox="0 0 6 8"><polygon points="0,0 6,4 0,8"/></svg></div>
</section>

<section class="banner rect" aria-label="Korvel medium rectangle banner">
  <svg class="bands" viewBox="0 0 375 375" preserveAspectRatio="none" aria-hidden="true">
    <polygon class="band-blue" points="0,0 375,0 375,166 0,201"/>
    <polygon class="band-red" points="0,201 375,166 375,180 0,224"/>
  </svg>
  <div class="wave-area" role="img" aria-label="Soft light blue flowing line decoration"></div>
  <h2 class="headline">Create your own<br>ecommerce website<br>@minimum $10/month</h2>
  <p class="subline">&amp; Start earning at the same time.</p>
  <p class="tagline">Revolutionary single<br>line affiliate program</p>
  <div class="brand">KORVEL</div>
  <div class="signup">Free sign up <svg width="6" height="8" viewBox="0 0 6 8"><polygon points="0,0 6,4 0,8"/></svg></div>
</section>

<section class="banner square" aria-label="Korvel square banner">
  <svg class="bands" viewBox="0 0 188 186" preserveAspectRatio="none" aria-hidden="true">
    <polygon class="band-blue" points="0,0 188,0 188,76 0,93"/>
    <polygon class="band-red" points="0,93 188,76 188,90 0,108"/>
  </svg>
  <h2 class="headline">Ecommerce<br>website<br>@10/month</h2>
  <p class="tagline">Revolutionary single<br>line affiliate program</p>
  <div class="brand">KORVEL</div>
  <div class="signup">Free sign up <svg width="4" height="6" viewBox="0 0 6 8"><polygon points="0,0 6,4 0,8"/></svg></div>
</section>

<section class="banner vertical" aria-label="Korvel vertical banner">
  <svg class="bands" viewBox="0 0 179 239" preserveAspectRatio="none" aria-hidden="true">
    <polygon class="band-blue" points="0,0 179,0 179,76 0,100"/>
    <polygon class="band-red" points="0,100 179,76 179,94 0,112"/>
  </svg>
  <div class="wave-area" role="img" aria-label="Soft light blue flowing line decoration"></div>
  <h2 class="headline">Ecommerce<br>website @minimum<br>$10/month</h2>
  <p class="tagline">Revolutionary<br>single line<br>affiliate program</p>
  <div class="brand">KORVEL</div>
  <div class="signup">Free sign up <svg width="4" height="6" viewBox="0 0 6 8"><polygon points="0,0 6,4 0,8"/></svg></div>
</section>

<section class="banner small" aria-label="Korvel small banner">
  <svg class="bands" viewBox="0 0 179 135" preserveAspectRatio="none" aria-hidden="true">
    <polygon class="band-blue" points="0,0 179,0 179,42 0,54"/>
    <polygon class="band-red" points="0,54 179,42 179,51 0,63"/>
  </svg>
  <h2 class="headline">Ecommerce website<br>@minimum 10/month</h2>
  <p class="tagline">Revolutionary single<br>line affiliate program</p>
  <div class="brand">KORVEL</div>
  <div class="signup">Free sign up <svg width="4" height="6" viewBox="0 0 6 8"><polygon points="0,0 6,4 0,8"/></svg></div>
</section>

<section class="banner leader" aria-label="Korvel leaderboard banner">
  <svg class="bands" viewBox="0 0 701 89" preserveAspectRatio="none" aria-hidden="true">
    <polygon class="band-blue" points="0,0 701,0 701,46 0,89"/>
    <polygon class="band-red" points="0,89 701,46 701,58 160,89"/>
  </svg>
  <div class="line-area" role="img" aria-label="Fine diagonal line decoration"></div>
  <h2 class="headline">Ecommerce website @minimum $10/month</h2>
  <p class="subline">Revolutionary single line affiliate program</p>
  <div class="brand on-blue">KORVEL</div>
  <div class="signup">Free sign up <svg width="6" height="8" viewBox="0 0 6 8"><polygon points="0,0 6,4 0,8"/></svg></div>
</section>

</body>
</html>
```